Profi-Kistenhof
Zielgruppe
Profi-Kistenhof.de vermietet Lagercontainern an Privatkunden und Gewerbetriebende
Vermietung von Stellfächen für Wohnmobile/Boote etc
Das ganze auf einem Gewerbegelände in Köln (Brauweiler)
Aufgabenstellung
Erstellung eines 2-Seitigen DIN lang (10,5 x 21 cm) Flyers
Seite A: Vermietung von Lagercontainern
Seite B: Stellfächen für Wohnmobile/Boote
Wichtig: Die Sicherheit (Zutrittskontrolle, Videoüberwachung, Brandmeldeanlage)
Preise sollen auf Flyern erscheinen, diese wie auch die Textee möchte ich jedoch ändern können.
Alle Texte können auch von der Seite profi-kistenhof.de übernommen werden
Das Logo (siehe boxen_welten.ai) müsste noch bearbeitet werden .... also "boxenwelten" raus und dafür "Lagerraum Container" rein
Gerne mit Symbolen arbeiten ..

```html
<!DOCTYPE html>
<html lang="de">
<head>
<meta charset="utf-8">
<title>Profi-Kistenhof – Flyer</title>
<link href="https://fonts.googleapis.com/css2?family=Ubuntu:wght@400;500;700&display=swap" rel="stylesheet">
<style>
:root{
  --green:#0e6b35;
  --green-soft:#e5eee9;
  --green-foot:#8fb39d;
  --blue:#0b68ad;
  --blue-soft:#e3eef7;
  --blue-foot:#8db5d6;
  --navy:#1d3557;
  --ink:#222;
  --grey-top:#ffffff;
  --grey-bottom:#d9d9d9;
  --white:#ffffff;
}
*{margin:0;padding:0;box-sizing:border-box}
html,body{width:1200px;height:936px;overflow:hidden;background:var(--white)}
body{position:relative;font-family:"Ubuntu",sans-serif;color:var(--ink)}
.flyer{position:absolute;top:42px;width:421px;height:809px;overflow:hidden}
.flyer--container{left:75px;--accent:var(--green);--soft:var(--green-soft);--foot:var(--green-foot)}
.flyer--parking{left:688px;--accent:var(--blue);--soft:var(--blue-soft);--foot:var(--blue-foot)}
.flyer__head{position:absolute;left:0;top:0;width:100%;background:linear-gradient(var(--grey-top) 0%,var(--grey-bottom) 100%)}
.flyer--container .flyer__head{height:297px}
.flyer--parking .flyer__head{height:291px}
.flyer__body{position:absolute;left:0;bottom:0;width:100%;background:var(--accent)}
.flyer--container .flyer__body{top:297px}
.flyer--parking .flyer__body{top:291px}
.brand{position:absolute;right:29px;top:0;text-align:right}
.brand__mark{display:flex;align-items:center;justify-content:flex-end;gap:8px;height:56px}
.brand__square{width:22px;height:22px;background:var(--navy);border-radius:3px}
.brand__name{font-size:17px;font-weight:700;color:var(--navy)}
.brand__site{font-size:17px;font-weight:700;color:var(--navy);margin-top:10px}
.brand__contact{font-size:11px;line-height:20px;margin-top:4px;color:#333}
.visual{position:absolute}
.flyer--container .visual{left:38px;top:82px;width:155px;height:144px;background:linear-gradient(90deg,#2c3570 0%,#6d5a40 45%,#a68a5e 60%,#b9bcc2 100%)}
.flyer--parking .visual{left:39px;top:60px;width:184px;height:128px;border-radius:24px 30px 8px 8px;background:linear-gradient(180deg,#f4f4f4 0%,#cfd2d6 100%)}
.title{position:absolute;left:31px;color:var(--accent);font-weight:700}
.flyer--container .title{top:245px;font-size:21px}
.flyer--parking .title{top:205px;font-size:28px;line-height:36px;font-weight:500}
.intro{position:absolute;left:31px;right:20px;color:var(--white);font-size:13px;line-height:17px}
.flyer--container .intro{top:312px}
.flyer--parking .intro{top:306px}
.features{position:absolute;left:31px;list-style:none;color:var(--white);font-size:15.5px}
.flyer--container .features{top:406px}
.flyer--parking .features{top:402px}
.features li{display:flex;align-items:center;gap:9px;height:29.7px}
.tick{width:11px;height:11px;flex:none}
.symbol{position:absolute}
.flyer--container .symbol{left:295px;top:488px;width:86px;height:67px}
.flyer--parking .symbol{left:292px;top:475px;width:78px;height:79px}
.price{position:absolute;background:var(--soft);color:var(--accent)}
.flyer--container .price{left:28px;top:591px;width:363px;height:120px}
.flyer--parking .price{left:29px;top:588px;width:362px;height:118px}
.price__amount{position:absolute;left:15px;top:9px;font-size:19px;font-weight:700}
.price__offer{position:absolute;left:15px;top:42px;font-size:13px}
.price__note{position:absolute;left:15px;top:66px;font-size:7.5px;line-height:11px}
.claim{position:absolute;left:0;width:100%;display:flex;justify-content:center;gap:18px;color:var(--foot);font-size:21px;font-weight:500}
.flyer--container .claim{top:745px}
.flyer--parking .claim{top:741px}
.claim span{display:flex;align-items:center;gap:6px}
.claim svg{width:13px;height:13px}
</style>
</head>
<body>

<section class="flyer flyer--container">
  <div class="flyer__head"></div>
  <div class="flyer__body"></div>
  <div class="brand">
    <div class="brand__mark"><span class="brand__square"></span><span class="brand__name">Profi-Kistenhof</span></div>
    <div class="brand__site">Profi-Kistenhof.de</div>
    <div class="brand__contact">Tel.: 0221 5550147<br>info@profi-kistenhof.de</div>
  </div>
  <div class="visual" role="img" aria-label="Offener Lagercontainer mit Holzkisten"></div>
  <h1 class="title">Vermietung von Lagercontainern</h1>
  <p class="intro">Profi-Kistenhof vermietet Container<br>zu kleinem Preis und Top-Konditionen<br>für die Lagerung privater oder gewerblicher Güter -<br>auch als kurzfristige Lösung (z.B. bei Umzug) geeignet.</p>
  <ul class="features">
    <li><svg class="tick" viewBox="0 0 12 12"><path d="M1.5 6.5l3 3 6-7" fill="none" stroke="#fff" stroke-width="2"/></svg>Rund um die Uhr zugänglich</li>
    <li><svg class="tick" viewBox="0 0 12 12"><path d="M1.5 6.5l3 3 6-7" fill="none" stroke="#fff" stroke-width="2"/></svg>14m³ bzw. 33m³ Kapazität</li>
    <li><svg class="tick" viewBox="0 0 12 12"><path d="M1.5 6.5l3 3 6-7" fill="none" stroke="#fff" stroke-width="2"/></svg>Zutrittskontrolle</li>
    <li><svg class="tick" viewBox="0 0 12 12"><path d="M1.5 6.5l3 3 6-7" fill="none" stroke="#fff" stroke-width="2"/></svg>Videoüberwacht</li>
    <li><svg class="tick" viewBox="0 0 12 12"><path d="M1.5 6.5l3 3 6-7" fill="none" stroke="#fff" stroke-width="2"/></svg>14 Tage Kündigungsfrist</li>
  </ul>
  <svg class="symbol" viewBox="0 0 86 67" aria-hidden="true">
    <g fill="#fff" stroke="#cfd8d2" stroke-width="1">
      <rect x="14" y="2" width="30" height="30"/>
      <rect x="2" y="33" width="30" height="32"/>
      <rect x="33" y="33" width="30" height="32"/>
      <rect x="54" y="22" width="28" height="28"/>
    </g>
  </svg>
  <div class="price">
    <div class="price__amount">148,- € pro Monat*</div>
    <div class="price__offer">1 Monat gratis bei einer Anmietung ab 3 Monaten</div>
    <div class="price__note">* Preis gilt pro Monat und Container für private Vermietung,<br>bei gewerblicher Anmietung zzgl. 19% MwSt.</div>
  </div>
  <div class="claim">
    <span><svg viewBox="0 0 12 12"><path d="M1.5 6.5l3 3 6-7" fill="none" stroke="currentColor" stroke-width="2"/></svg>günstig</span>
    <span><svg viewBox="0 0 12 12"><path d="M1.5 6.5l3 3 6-7" fill="none" stroke="currentColor" stroke-width="2"/></svg>sicher</span>
    <span><svg viewBox="0 0 12 12"><path d="M1.5 6.5l3 3 6-7" fill="none" stroke="currentColor" stroke-width="2"/></svg>lagern</span>
  </div>
</section>

<section class="flyer flyer--parking">
  <div class="flyer__head"></div>
  <div class="flyer__body"></div>
  <div class="brand">
    <div class="brand__mark"><span class="brand__square"></span><span class="brand__name">Profi-Kistenhof</span></div>
    <div class="brand__site">Profi-Kistenhof.de</div>
    <div class="brand__contact">Tel.: 0221 5550147<br>info@profi-kistenhof.de</div>
  </div>
  <div class="visual" role="img" aria-label="Weißes Wohnmobil"></div>
  <h1 class="title">Stellfächen für<br>Wohnmobile/Boote</h1>
  <p class="intro">Profi-Kistenhof vermietet Stellfächen für Wohnmobile<br>oder Boote zu kleinem Preis und Top-Konditionen - auch<br>als kurzfristige Lösung (z.B. bei Umzug) geeignet.</p>
  <ul class="features">
    <li><svg class="tick" viewBox="0 0 12 12"><path d="M1.5 6.5l3 3 6-7" fill="none" stroke="#fff" stroke-width="2"/></svg>Rund um die Uhr zugänglich</li>
    <li><svg class="tick" viewBox="0 0 12 12"><path d="M1.5 6.5l3 3 6-7" fill="none" stroke="#fff" stroke-width="2"/></svg>Zutrittskontrolle</li>
    <li><svg class="tick" viewBox="0 0 12 12"><path d="M1.5 6.5l3 3 6-7" fill="none" stroke="#fff" stroke-width="2"/></svg>Videoüberwacht</li>
    <li><svg class="tick" viewBox="0 0 12 12"><path d="M1.5 6.5l3 3 6-7" fill="none" stroke="#fff" stroke-width="2"/></svg>Brandmeldeanlage</li>
    <li><svg class="tick" viewBox="0 0 12 12"><path d="M1.5 6.5l3 3 6-7" fill="none" stroke="#fff" stroke-width="2"/></svg>14 Tage Kündigungsfrist</li>
  </ul>
  <svg class="symbol" viewBox="0 0 78 79" aria-hidden="true">
    <rect x="1.5" y="1.5" width="75" height="76" rx="7" fill="#fff" stroke="#111" stroke-width="3"/>
    <path d="M12 24h44l6 10h4v18H12z" fill="#111"/>
    <rect x="18" y="30" width="10" height="8" fill="#fff"/>
    <rect x="34" y="30" width="8" height="14" fill="#fff"/>
    <circle cx="24" cy="54" r="6" fill="#111" stroke="#fff" stroke-width="2"/>
    <circle cx="54" cy="54" r="6" fill="#111" stroke="#fff" stroke-width="2"/>
  </svg>
  <div class="price">
    <div class="price__amount">148,- € pro Monat*</div>
    <div class="price__offer">1 Monat gratis bei einer Anmietung ab 3 Monaten</div>
    <div class="price__note">* Preis gilt pro Monat und Container für private Vermietung,<br>bei gewerblicher Anmietung zzgl. 19% MwSt.</div>
  </div>
  <div class="claim">
    <span><svg viewBox="0 0 12 12"><path d="M1.5 6.5l3 3 6-7" fill="none" stroke="currentColor" stroke-width="2"/></svg>günstig</span>
    <span><svg viewBox="0 0 12 12"><path d="M1.5 6.5l3 3 6-7" fill="none" stroke="currentColor" stroke-width="2"/></svg>sicher</span>
    <span><svg viewBox="0 0 12 12"><path d="M1.5 6.5l3 3 6-7" fill="none" stroke="currentColor" stroke-width="2"/></svg>lagern</span>
  </div>
</section>

</body>
</html>
```